Software as a Service to manage Home Care Management

We need a web site designed for Home Care Management Software as a Service product, that facilitates Home Care organizations to manage and schedule carers to visit client homes. We want a modern look and feel using our existing logo.

Target Market(s)

Home Care Management organizations. Product is similar to: https://kelvantro.co/

Coding

Coded - Design and coding required

Number of Pages Required

3 page

```html
<!DOCTYPE html>
<html lang="en">
<head>
<meta charset="utf-8">
<title>Carevista – Home Care Management</title>
<link rel="stylesheet" href="https://fonts.googleapis.com/css2?family=Cinzel:wght@400;600&family=Lato:wght@400;700&display=swap">
<style>
:root{
  --pink:#f2558b;
  --pink-dark:#e2386f;
  --ink:#2b2b2b;
  --text:#444;
  --muted:#8a8a8a;
  --grey-band:#efefef;
  --dark:#555558;
  --white:#fff;
}
*{box-sizing:border-box;margin:0;padding:0}
html,body{width:1200px;height:4854px;overflow:hidden}
body{font-family:"Lato",sans-serif;color:var(--text);background:var(--white);position:relative}
section,header,footer{position:absolute;left:0;width:1200px}
.serif{font-family:"Cinzel",serif;font-weight:400;color:var(--ink)}
.btn{position:absolute;background:var(--pink);color:#fff;font-weight:700;font-size:15px;display:flex;align-items:center;justify-content:center;letter-spacing:.5px}
.btn.grey{background:#5d5d5d}

/* header */
.site-header{top:0;height:98px;background:#fff}
.brand{position:absolute;left:62px;top:24px;display:flex;align-items:center;gap:10px}
.brand-mark{width:40px;height:40px;border-radius:50%;background:var(--pink)}
.brand-name{font-family:"Cinzel",serif;font-size:28px;color:#333;line-height:1}
.brand-tag{font-size:10px;letter-spacing:4px;color:#777;margin-top:4px}
.nav{position:absolute;left:386px;top:40px;font-size:15px;color:#444}
.nav a{color:inherit;text-decoration:none;position:absolute;white-space:nowrap}
.nav .active{color:var(--pink)}
.demo{left:994px;top:31px;width:156px;height:38px;font-weight:400}

/* hero */
.hero{top:98px;height:690px;background:linear-gradient(100deg,#d8c7b6 0%,#efe6da 35%,#e8ddd0 65%,#cbb6a0 100%)}
.hero-photo{position:absolute;inset:0}
.hero-card{position:absolute;left:98px;top:190px;width:475px;height:245px;background:rgba(242,85,139,.93);border-radius:60px 0 60px 0;padding:46px 0 0 72px;color:#fff}
.hero-card small{font-size:16px;letter-spacing:1px}
.hero-card h1{font-family:"Cinzel",serif;font-weight:400;font-size:37px;line-height:42px;margin-top:10px}
.dots{position:absolute;left:582px;top:637px;display:flex;gap:12px}
.dots i{width:16px;height:16px;border-radius:50%;background:#fff}
.dots i.on{background:var(--pink)}

/* about */
.about{top:788px;height:580px;background:#f4f4f4}
.about-photo{position:absolute;left:0;top:0;width:882px;height:580px;background:linear-gradient(90deg,#c9b2a2,#eadfd6 60%,#f4f4f4)}
.about h2{position:absolute;left:646px;top:112px;font-size:38px}
.about p{position:absolute;left:646px;top:193px;width:475px;font-size:15.5px;line-height:27.5px;color:#333}
.about .btn{left:640px;top:385px;width:176px;height:48px}

/* why */
.why{top:1368px;height:612px;background:linear-gradient(100deg,#f0508a,#f56595 55%,#f2558b)}
.why h2{position:absolute;width:100%;top:55px;text-align:center;color:#fff;font-size:36px}
.rule{position:absolute;height:4px;background:#fff;width:58px}
.tablet{position:absolute;left:109px;top:182px;width:475px;height:330px;border-radius:20px;background:#f4f4f4;box-shadow:0 10px 30px rgba(0,0,0,.2)}
.feature{position:absolute;left:640px;width:520px;height:110px}
.feature-icon{position:absolute;left:0;top:0;width:110px;height:110px}
.feature h3{position:absolute;left:129px;top:22px;color:#fff;font-size:19px;font-weight:700}
.feature p{position:absolute;left:129px;top:52px;color:#fff;font-size:13.5px;line-height:17px;width:310px}

/* optimised */
.optimised{top:1980px;height:626px;background:#fff}
.optimised h2{position:absolute;left:113px;top:115px;font-size:38px;line-height:48px;width:560px}
.optimised p{position:absolute;left:109px;width:494px;font-size:15.5px;line-height:28px;text-align:justify;color:#333}
.optimised .btn{left:107px;top:450px;width:189px;height:47px}
.phone{position:absolute;left:772px;top:74px;width:240px;height:480px;border-radius:34px;background:#111;padding:10px}
.screen{width:100%;height:100%;border-radius:26px;background:#fff;overflow:hidden;position:relative;font-size:11px}

/* numbers */
.numbers{top:2606px;height:642px;background:var(--grey-band)}
.numbers h2{position:absolute;width:100%;top:68px;text-align:center;font-size:30px}
.numbers h2 b{font-weight:600}
.card{position:absolute;top:148px;width:320px;height:388px;background:#fff}
.card-photo{position:absolute;left:0;top:0;width:100%;height:200px}
.badge{position:absolute;left:110px;top:150px;width:100px;height:100px;border-radius:50%;background:var(--pink);color:#fff;font-size:28px;display:flex;align-items:center;justify-content:center}
.badge.grey{background:#5d5d5d}
.card h4{position:absolute;top:276px;width:100%;text-align:center;font-size:15.5px;font-weight:400;line-height:21px;color:#333}
.card .btn{top:321px;left:70px;width:160px;height:40px;font-weight:400;font-family:"Cinzel",serif;font-size:14px}

/* partners */
.partners{top:3248px;height:526px;background:#fff}
.partners h2{position:absolute;width:100%;top:120px;text-align:center;font-size:30px}
.partners h2 b{font-weight:600}
.line-pink{position:absolute;top:141px;height:4px;width:48px;background:var(--pink)}
.partner{position:absolute;width:180px;text-align:center;font-size:24px;font-weight:700;color:#888}

/* contact */
.contact{top:3774px;height:635px;background:var(--dark)}
.contact h2{position:absolute;width:100%;top:82px;text-align:center;color:#fff;font-size:35px}
.contact .lead{position:absolute;width:100%;top:149px;text-align:center;color:#fff;font-size:17px}
.field{position:absolute;background:#fff;color:#666;font-size:16px;padding:20px 28px}
.contact .btn{left:492px;top:495px;width:216px;height:62px;font-size:17px}

/* footer */
.site-footer{top:4409px;height:358px;background:#fff}
.foot-brand{position:absolute;left:112px;top:80px;width:240px;text-align:center}
.foot-brand .mark{width:70px;height:70px;border-radius:50%;background:#d7d7d7;margin:0 auto 18px}
.foot-brand .name{font-family:"Cinzel",serif;font-size:37px;color:#777;line-height:1}
.foot-brand .tag{font-size:12px;letter-spacing:4px;color:#888;margin-top:4px}
.col{position:absolute;top:98px}
.col h5{font-size:16px;color:#444;font-weight:700;letter-spacing:.5px;margin-bottom:14px}
.col a{display:block;font-size:15.5px;color:#777;text-decoration:none;line-height:32px}
.social a{display:flex;align-items:center;gap:14px;line-height:46px}
.social i{width:18px;height:18px;border-radius:50%;background:var(--pink);display:inline-block}
.legal{position:absolute;top:4767px;left:0;width:1200px;height:87px;background:#ececec;text-align:center;font-size:15px;color:#555;line-height:87px}
</style>
</head>
<body>

<header class="site-header">
  <div class="brand">
    <span class="brand-mark"></span>
    <div><div class="brand-name">Carevista</div><div class="brand-tag">HOME CARE MANAGEMENT</div></div>
  </div>
  <nav class="nav">
    <a class="active" style="left:0">ABOUT</a>
    <a style="left:100px">PRODUCT</a>
    <a style="left:220px">PRICING</a>
    <a style="left:328px">FAQ</a>
    <a style="left:406px">CONTACT</a>
    <a style="left:526px">LOGIN</a>
  </nav>
  <a class="btn demo">BOOK DEMO</a>
</header>

<section class="hero">
  <div class="hero-photo" role="img" aria-label="Photo of a young carer and two smiling elderly clients looking at a laptop on a sofa"></div>
  <div class="hero-card">
    <small>CAREVISTA SOFTWARE</small>
    <h1>SCHEDULE CARERS<br>TO VISIT CLIENT<br>HOMES EASILY</h1>
  </div>
  <div class="dots"><i></i><i class="on"></i><i></i></div>
</section>

<section class="about">
  <div class="about-photo" role="img" aria-label="Photo of a carer with her hands on the shoulders of a smiling elderly woman"></div>
  <h2 class="serif">CAREVISTA</h2>
  <p>Lorem ipsum dolor sit amet, consectetur adipiscing elit, sed do eiusmod tempor incididunt ut labore et dolore magna aliqua. Ut enim ad minim veniam, quis nostrud exercitation ullamco laboris nisi ut aliquip ex ea commodo consequat. Duis aute irure dolor in reprehenderit in voluptate velit esse cillum dolore eu fugiat nulla pariatur. Excepteur sint o</p>
  <a class="btn">LEARN MORE ›</a>
</section>

<section class="why">
  <h2 class="serif" style="color:#fff">WHY CAREVISTA</h2>
  <span class="rule" style="left:571px;top:110px"></span>
  <div class="tablet">
    <svg width="475" height="330" viewBox="0 0 475 330">
      <rect x="30" y="24" width="420" height="282" fill="#fff"/>
      <rect x="40" y="34" width="195" height="98" fill="#c6317a"/>
      <polyline points="90,90 110,70 130,95 150,60 170,88 190,66 215,80" fill="none" stroke="#fff" stroke-width="2"/>
      <text x="48" y="80" fill="#fff" font-size="20" font-family="Lato">25</text>
      <rect x="245" y="34" width="100" height="262" fill="#fafafa"/>
      <rect x="355" y="34" width="85" height="262" fill="#fafafa"/>
      <circle cx="272" cy="120" r="18" fill="none" stroke="#e8467e" stroke-width="4"/>
      <circle cx="310" cy="190" r="18" fill="none" stroke="#e8467e" stroke-width="4"/>
      <g fill="#e8467e"><rect x="255" y="250" width="8" height="30"/><rect x="268" y="240" width="8" height="40"/><rect x="281" y="228" width="8" height="52"/><rect x="294" y="258" width="8" height="22"/><rect x="307" y="236" width="8" height="44"/><rect x="320" y="250" width="8" height="30"/></g>
      <polygon points="48,170 65,158 78,168 95,154 95,180 48,180" fill="#e8467e"/>
      <polygon points="140,170 155,160 170,168 185,155 185,180 140,180" fill="#e8467e"/>
      <g fill="none" stroke="#e8467e" stroke-width="2"><circle cx="75" cy="220" r="12"/><circle cx="130" cy="220" r="12"/><circle cx="185" cy="220" r="12"/></g>
      <g fill="#e8467e"><rect x="60" y="280" width="30" height="6" rx="3"/><rect x="115" y="280" width="30" height="6" rx="3"/><rect x="170" y="280" width="30" height="6" rx="3"/></g>
    </svg>
  </div>
  <div class="feature" style="top:198px">
    <svg class="feature-icon" viewBox="0 0 110 110"><circle cx="58" cy="55" r="38" fill="#fff"/><circle cx="58" cy="46" r="10" fill="none" stroke="#f2558b" stroke-width="3"/><path d="M40 76 q18-22 36 0" fill="none" stroke="#f2558b" stroke-width="3"/></svg>
    <h3>FOR CARERS</h3><p>olor in reprehenderit in voluptate velit esse cillum dolore eu fugiat</p>
  </div>
  <div class="feature" style="top:328px">
    <svg class="feature-icon" viewBox="0 0 110 110"><circle cx="58" cy="55" r="38" fill="#fff"/><path d="M58 72 L42 56 a9 9 0 0 1 16-12 a9 9 0 0 1 16 12 Z" fill="none" stroke="#f2558b" stroke-width="3"/></svg>
    <h3>FOR CLIENTS</h3><p>olor in reprehenderit in voluptate velit esse cillum dolore eu fugiat</p>
  </div>
  <div class="feature" style="top:445px">
    <svg class="feature-icon" viewBox="0 0 110 110"><circle cx="58" cy="55" r="38" fill="#fff"/><path d="M42 56 L58 42 L74 56 V72 H42 Z" fill="none" stroke="#f2558b" stroke-width="3"/></svg>
    <h3>FOR MANGERS</h3><p>olor in reprehenderit in voluptate velit esse cillum dolore eu fugiat</p>
  </div>
</section>

<section class="optimised">
  <h2 class="serif">OPTIMISED HOME CARE SOFTWARE</h2>
  <p style="top:230px">Lorem ipsum dolor sit amet, consectetur adipiscing elit, sed do eiusmod tempor incididunt ut labore et dolore magna aliqua. Ut enim ad minim veniam, quis nostrud exercitation ullamco laboris nisi ut aliquip ex ea commodo consequat.</p>
  <p style="top:360px">Duis aute irure dolor in reprehenderit in voluptate velit esse cillum dolore eu fugiat nulla pariatur. Excepteur sint occaecat</p>
  <a class="btn">BOOK NOW ›</a>
  <div class="phone">
    <div class="screen">
      <div style="background:#1a5f8f;color:#fff;height:42px;padding:16px 14px;font-size:11px">Carter … <b>Visits</b></div>
      <div style="margin:8px;border:1px solid #ccd;height:40px;text-align:center;color:#8aa;padding-top:6px">Wed 17 Apr<br><span style="font-size:9px">08:00-16:00</span></div>
      <div style="padding:6px 14px;color:#222"><b>Nora Palmer</b><br><span style="font-size:10px">13:40 - 14:10 · 30 min</span></div>
      <div style="padding:10px 14px;font-size:9px;color:#888">Work shift: 08:00 - 16:00</div>
      <div style="margin:2px 60px;background:#3aa6d8;color:#fff;text-align:center;padding:6px;font-size:9px">Report mileage</div>
      <div style="padding:18px 14px;font-size:9px;color:#999">Updated 13:44 · Hours 0h</div>
      <div style="margin:4px 60px;background:#3aa6d8;color:#fff;text-align:center;padding:6px;font-size:9px">+ Create visit</div>
      <div style="margin:14px 60px;background:#3aa6d8;color:#fff;text-align:center;padding:6px;font-size:9px">+ Create event</div>
    </div>
  </div>
</section>

<section class="numbers">
  <h2 class="serif"><b>SUCCESS</b> IN NUMBERS</h2>
  <span class="rule" style="left:573px;top:112px;background:var(--pink);width:52px"></span>
  <div class="card" style="left:117px">
    <div class="card-photo" role="img" aria-label="Photo of a carer helping an elderly man in a wheelchair" style="background:linear-gradient(120deg,#d9d3cc,#9aa6b2)"></div>
    <div class="badge">14M</div>
    <h4>TOTAL CARE HOURS<br>MANAGED BY CAREVISTA</h4>
    <a class="btn">READ MORE ›</a>
  </div>
  <div class="card" style="left:460px">
    <div class="card-photo" role="img" aria-label="Photo of a nurse showing a tablet to an elderly man" style="background:linear-gradient(120deg,#a9a59c,#d8d2c6)"></div>
    <div class="badge grey">88%</div>
    <h4>CUSTOMER SUPPORT<br>HAPPINESS</h4>
    <a class="btn grey">READ MORE ›</a>
  </div>
  <div class="card" style="left:803px">
    <div class="card-photo" role="img" aria-label="Photo of a young woman and an elderly man using a laptop together" style="background:linear-gradient(120deg,#c9cdd2,#e7ddd2)"></div>
    <div class="badge">20K</div>
    <h4>ACTIVE CAREVISTA<br>USERS</h4>
    <a class="btn">READ MORE ›</a>
  </div>
</section>

<section class="partners">
  <span class="line-pink" style="left:270px"></span>
  <h2 class="serif">WORKING IN <b>ASSOCIATION</b> WITH</h2>
  <span class="line-pink" style="left:882px"></span>
  <div class="partner" style="left:70px;top:228px">Orvane</div>
  <div class="partner" style="left:282px;top:228px">Tradelux</div>
  <div class="partner" style="left:496px;top:228px">Homequarter</div>
  <div class="partner" style="left:708px;top:228px">Brightcast</div>
  <div class="partner" style="left:920px;top:228px">Sportwave</div>
  <div class="partner" style="left:70px;top:342px">Starmill</div>
  <div class="partner" style="left:282px;top:342px">Leadcircle</div>
  <div class="partner" style="left:496px;top:342px">Northway Realty</div>
  <div class="partner" style="left:708px;top:342px">Lumessa</div>
  <div class="partner" style="left:920px;top:342px">Ironvale</div>
</section>

<section class="contact">
  <h2 class="serif" style="color:#fff">CONTACT US</h2>
  <div class="lead">Get a full overview of the Kelvantro Care Management platform.</div>
  <div class="field" style="left:188px;top:213px;width:407px;height:56px">First name</div>
  <div class="field" style="left:612px;top:213px;width:407px;height:56px">Last name</div>
  <div class="field" style="left:188px;top:286px;width:407px;height:56px">Phone</div>
  <div class="field" style="left:612px;top:286px;width:407px;height:56px">Email</div>
  <div class="field" style="left:185px;top:357px;width:834px;height:114px">Message</div>
  <a class="btn">SUBMIT NOW ›</a>
</section>

<footer class="site-footer">
  <div class="foot-brand"><div class="mark"></div><div class="name">Carevista</div><div class="tag">HOME CARE MANAGEMENT</div></div>
  <div class="col" style="left:436px"><h5>CAREVISTA</h5><a>Home</a><a>About Us</a><a>Our Pricing</a><a>Support</a></div>
  <div class="col" style="left:674px"><h5>CONTACT US</h5><a>Support</a><a>FAQ</a><a>Why Us</a><a>Testimonials</a></div>
  <div class="col social" style="left:930px"><h5>FOLLOW US</h5><a><i></i>Friendloop</a><a><i></i>Chirpline</a><a><i></i>Snapframe</a></div>
</footer>
<div class="legal">© 2020 Carevista &nbsp;|&nbsp; Term of USe &nbsp;|&nbsp; Privacy</div>

</body>
</html>
```